Graphic design for the use of marketing mainly in the form of promotional die cut stickers

I’m looking for a promotional design that incorporates business logo and phone number. My business is mobile mechanical repairs to earthmoving and mining equipment. Interests would also include images of services provided like earthmoving and mining equipment either reality or cartoon. Please don’t restrict yourself to the images provided as I’m always attracted to seeing the passion of the artist show through their work.
Updates

Phone number is 0four58149263

Target Market(s)

Similar people in the same industry

Industry/Entity Type

Mining, earthmoving, mechanical, diesel fitter

Requirements
Must have
• Business logo and phone number

```html
<!DOCTYPE html>
<html lang="en">
<head>
<meta charset="utf-8">
<title>Kestrel Diesel Pty Ltd – Promotional Sticker</title>
<link rel="stylesheet" href="https://fonts.googleapis.com/css2?family=Russo+One&family=Orbitron:wght@500;800&display=swap">
<style>
  :root {
    --backdrop: #a3a3a3;
    --ink: #111011;
    --paper: #ffffff;
    --signal-red: #e81116;
    --subtext-grey: #5e5e5e;
    --art-dark: #1c1b1c;
    --art-deep: #0b0a0b;
  }
  * { margin: 0; padding: 0; box-sizing: border-box; }
  html, body {
    width: 1200px;
    height: 960px;
    overflow: hidden;
    background: var(--backdrop);
  }
  .canvas {
    position: relative;
    width: 1200px;
    height: 960px;
  }
  .sticker {
    position: absolute;
    left: 256px;
    top: 177px;
    width: 687px;
    height: 597px;
    border-radius: 15px;
    overflow: hidden;
    background: var(--paper);
    box-shadow: 2px 4px 8px rgba(0, 0, 0, 0.35);
  }
  .band { position: absolute; left: 0; width: 100%; }
  .band--machinery { top: 0; height: 212px; background: var(--ink); }
  .band--brand { top: 212px; height: 219px; background: var(--paper); }
  .band--service {
    top: 431px; height: 64px; background: var(--ink);
    display: flex; align-items: center; justify-content: center;
  }
  .band--phone {
    top: 495px; height: 102px; background: var(--signal-red);
    display: flex; align-items: center; justify-content: center;
  }
  .machinery-art {
    position: absolute;
    left: 52px;
    top: 14px;
    width: 590px;
    height: 233px;
    border-radius: 6px;
    background: linear-gradient(160deg, var(--art-dark), var(--art-deep));
  }
  .brand-dot {
    position: absolute;
    left: 23px;
    top: 244px;
    width: 166px;
    height: 166px;
    border-radius: 50%;
    background: var(--signal-red);
  }
  .brand-name {
    position: absolute;
    left: 210px;
    top: 260px;
    width: 460px;
    font-family: "Russo One", sans-serif;
    font-weight: 400;
    font-size: 88px;
    line-height: 88px;
    letter-spacing: 2px;
    color: var(--ink);
    white-space: nowrap;
  }
  .brand-descriptor {
    position: absolute;
    left: 201px;
    top: 342px;
    width: 470px;
    font-family: "Orbitron", sans-serif;
    font-weight: 500;
    font-size: 41px;
    line-height: 44px;
    letter-spacing: 0;
    color: var(--subtext-grey);
    white-space: nowrap;
  }
  .service-line {
    font-family: "Russo One", sans-serif;
    font-style: italic;
    font-size: 50px;
    letter-spacing: 2px;
    color: var(--paper);
    white-space: nowrap;
    transform: translateY(1px);
  }
  .phone-number {
    font-family: "Orbitron", sans-serif;
    font-weight: 800;
    font-size: 72px;
    letter-spacing: 2px;
    word-spacing: 8px;
    color: var(--paper);
    white-space: nowrap;
  }
</style>
</head>
<body>
  <main class="canvas">
    <section class="sticker">
      <div class="band band--machinery"></div>
      <div class="band band--brand"></div>
      <div class="machinery-art" role="img" aria-label="Line illustration of a crawler bulldozer and a mining haul truck, white outlines on black"></div>

      <div class="brand-dot" aria-hidden="true"></div>
      <h1 class="brand-name">KESTREL</h1>
      <p class="brand-descriptor">DIESEL PTY LTD</p>

      <div class="band band--service">
        <p class="service-line">MECHANICAL REPAIRS</p>
      </div>
      <div class="band band--phone">
        <p class="phone-number">0458 149 263</p>
      </div>
    </section>
  </main>
</body>
</html>
```